New Zealand health product business needs website designed

A website is required for a business that sells New Zealand made products, namely products like infant formula, health products such as NZ honey, supplements, skincare products etc. This is purely an informative website that will introduce the all the different types of products the business has to offer. The target audience will the the Chinese market. The logo is a calligraphy style font in colours 78b643 and 313542 (logo is still being finalised at the moment) so a colour theme to match would be great.

It is crucial that the design communicates the beautiful nature of New Zealand, non-polluted environments, with emphasis on pure, natural and cleaniness.
Updates

A website that I quite like is http://www.frostvalegelato.co.nz

Information is easy to find, layout is nice and clear.                          

Hi all, I have now uploaded a logo for the business "Tawny Crate", please note that this is yet to be finalized however I expect it to be minor changes so please ensure the website theme and colour use go well with the logo. 

There are three scenery images uploaded, designs with any one of them used is fine whichever works better with your design.  Only one image is required on the website, no sliding effects for this.

Also just to clarify my requirements further.  The developer can use HTML, PHP, Javascript, CSS for coding, preferably to have the images cut and a pdf guide provided for things like alignment and sizing etc.

The menu items are Home / Our story / Product outline / Brands / Contact us
Designs are required for all these.  Within the product outline page, the subcategories are -
Infant formulas
Baby supplements
Toddlers products
Honey
Beauty products
Mens supplements
Womens supplements
Health products
Others

   

Target Market(s)

China based customers looking for quality products from New Zealand.

Industry/Entity Type

Health

Requirements
Must have
• clear menu bar in home page, the four main menu items are -
Our story
Product outline
Brands
Contact us
Nice to have
• Space for a large scenery photo in the home page

```html
<!DOCTYPE html>
<html lang="en">
<head>
<meta charset="utf-8">
<title>Tawny Crate — Our Story</title>
<link rel="stylesheet" href="https://fonts.googleapis.com/css2?family=Arimo:wght@400&display=swap">
<style>
  :root {
    --nav-bg: rgba(40, 40, 40, 0.78);
    --nav-text: #f2f2f2;
    --panel-bg: rgba(30, 26, 20, 0.72);
    --panel-line: rgba(200, 200, 200, 0.55);
    --panel-text: #d8d8d8;
    --badge-bg: rgba(232, 224, 214, 0.92);
    --dot-active: #e6e6e6;
    --dot-idle: #8d8d8d;
    --footer-top: #2a2a2a;
    --footer-bottom: #050505;
    --footer-head: #a9a9a9;
    --footer-text: #c4c4c4;
    --footer-link: #ffffff;
    --sky: #dfe4ea;
    --snow: #c9ccd0;
    --slope: #8a6a2a;
    --lake: #2a6fae;
    --shore: #6e5a22;
  }
  * { margin: 0; padding: 0; box-sizing: border-box; }
  html, body { width: 1200px; height: 982px; overflow: hidden; background: #000; }
  body { font-family: "Arimo", Arial, sans-serif; position: relative; }

  .hero {
    position: absolute; left: 0; top: 0; width: 1200px; height: 802px;
    background: linear-gradient(180deg,
      var(--sky) 0%, var(--snow) 14%, #b89a58 24%, var(--slope) 38%,
      #7a5e24 50%, #3a5f86 54%, var(--lake) 62%, #2d76b8 70%,
      var(--shore) 76%, #5a4618 100%);
  }

  .site-nav {
    position: absolute; left: 0; top: 0; width: 1200px; height: 63px;
    background: var(--nav-bg);
  }
  .site-nav a {
    position: absolute; top: 22px; color: var(--nav-text);
    font-size: 16px; text-decoration: none; letter-spacing: 0.2px; white-space: nowrap;
  }
  .site-nav a.current { text-decoration: underline; text-underline-offset: 4px; }
  .nav-story { left: 239px; }
  .nav-products { left: 364px; }
  .nav-brands { left: 740px; }
  .nav-contact { left: 844px; }
  .brand-name {
    position: absolute; left: 520px; top: 19px; color: var(--nav-text);
    font-size: 20px; letter-spacing: 1px; white-space: nowrap;
  }

  .story-panel {
    position: absolute; left: 195px; top: 290px; width: 897px; height: 257px;
    background: var(--panel-bg);
  }
  .panel-rule {
    position: absolute; left: 17px; top: 16px; width: 863px; height: 1px;
    background: var(--panel-line);
  }
  .slide-dots { position: absolute; left: 92px; top: 34px; display: flex; gap: 3px; }
  .slide-dots span { width: 7px; height: 7px; border-radius: 50%; background: var(--dot-idle); }
  .slide-dots span.active { background: var(--dot-active); }
  .slide-arrows { position: absolute; left: 789px; top: 34px; }
  .story-text {
    position: absolute; left: 92px; top: 92px; width: 728px; height: 140px;
    overflow: hidden; color: var(--panel-text); font-size: 13.5px; line-height: 17.6px;
    text-align: justify; hyphens: auto;
  }
  .story-text p + p { margin-top: 17px; }

  .story-badge {
    position: absolute; left: 567px; top: 214px; width: 152px; height: 152px;
    border-radius: 50%; background: var(--badge-bg);
  }
  .badge-dot {
    position: absolute; left: 639px; top: 302px; width: 9px; height: 9px;
    border-radius: 50%; background: #6d6d6d;
  }

  .site-footer {
    position: absolute; left: 0; top: 802px; width: 1200px; height: 180px;
    background: linear-gradient(180deg, var(--footer-top), var(--footer-bottom));
  }
  .footer-col { position: absolute; top: 26px; width: 215px; }
  .footer-col h2 {
    font-weight: 400; font-size: 15px; color: var(--footer-head);
    text-decoration: underline; text-underline-offset: 3px;
  }
  .footer-col p {
    margin-top: 14px; font-size: 11.5px; line-height: 15.5px; color: var(--footer-text);
    height: 47px; overflow: hidden;
  }
  .read-more {
    display: inline-flex; align-items: center; gap: 7px; margin-top: 16px;
    color: var(--footer-link); font-size: 11.5px; text-decoration: none;
  }
  .col-one { left: 167px; }
  .col-two { left: 415px; }
  .col-three { left: 676px; }
  .product-shot {
    position: absolute; left: 915px; top: 21px; width: 130px; height: 122px;
    background: linear-gradient(180deg, #2f6fb8 0%, #d8e6f0 40%, #c9b23a 75%, #2a5fa0 100%);
    border-radius: 6px;
  }
  .copyright {
    position: absolute; left: 168px; top: 158px; font-size: 11px; color: var(--footer-text);
  }
</style>
</head>
<body>
  <div class="hero" role="img" aria-label="Landscape photo of snow-capped mountains above a deep blue lake with a grassy shore and a small white building"></div>

  <nav class="site-nav">
    <a class="nav-story current" href="#">Our Story</a>
    <a class="nav-products" href="#">Product Outline</a>
    <span class="brand-name">Tawny Crate</span>
    <a class="nav-brands" href="#">Brands</a>
    <a class="nav-contact" href="#">Contact us</a>
  </nav>

  <section class="story-panel">
    <div class="panel-rule"></div>
    <div class="slide-dots"><span class="active"></span><span></span><span></span><span></span></div>
    <svg class="slide-arrows" width="26" height="14" viewBox="0 0 26 14" aria-hidden="true">
      <polyline points="8,2 3,7 8,12" fill="none" stroke="#8a8a8a" stroke-width="2"/>
      <polyline points="18,2 23,7 18,12" fill="none" stroke="#e6e6e6" stroke-width="2"/>
    </svg>
    <div class="story-text">
      <p>Lorem ipsum dolor sit amet, consectetur adipiscing elit. Nulla tincidunt, massa tempor ultricies tristique, nibh lacus sodales nulla, sit amet tempus tellus libero vitae turpis. Sed vehicula nisi ut dui accumsan dignissim. Pellentesque fermentum, libero et placerat vestibulum, justo arcu egestas diam, eu mattis ante nisl non enim. Phasellus feugiat ante sit amet mi pretium vestibulum. In hac habitasse platea dictumst.</p>
      <p>Lorem ipsum dolor sit amet, consectetur adipiscing elit. Nulla tincidunt, massa tempor ultricies tristique, nibh lacus sodales nulla, sit amet tempus tellus libero vitae turpis. Sed vehicula nisi ut dui accumsan dignissim. Pellentesque fermentum, libero et placerat vestibulum.</p>
    </div>
  </section>
  <div class="story-badge" role="img" aria-label="Hand-lettered script heading reading Our Story"></div>
  <div class="badge-dot"></div>

  <footer class="site-footer">
    <div class="footer-col col-one">
      <h2>Section 1</h2>
      <p>Lorem ipsum dolor sit amet, consectetur adipiscing elit. Nulla tincidunt, massa tempor ultricies tristique, nibh lacus sodales</p>
      <a class="read-more" href="#">read more
        <svg width="22" height="6" viewBox="0 0 22 6" aria-hidden="true"><line x1="0" y1="3" x2="20" y2="3" stroke="#fff"/><polyline points="17,0.5 21,3 17,5.5" fill="none" stroke="#fff"/></svg></a>
    </div>
    <div class="footer-col col-two">
      <h2>Section 2</h2>
      <p>Lorem ipsum dolor sit amet, consectetur adipiscing elit. Nulla tincidunt, massa tempor ultricies tristique, nibh lacus sodales</p>
      <a class="read-more" href="#">read more
        <svg width="22" height="6" viewBox="0 0 22 6" aria-hidden="true"><line x1="0" y1="3" x2="20" y2="3" stroke="#fff"/><polyline points="17,0.5 21,3 17,5.5" fill="none" stroke="#fff"/></svg></a>
    </div>
    <div class="footer-col col-three">
      <h2>Featured Product</h2>
      <p>Lorem ipsum dolor sit amet, consectetur adipiscing elit. Nulla tincidunt, massa tempor ultricies tristique, nibh lacus sodales</p>
      <a class="read-more" href="#">read more
        <svg width="22" height="6" viewBox="0 0 22 6" aria-hidden="true"><line x1="0" y1="3" x2="20" y2="3" stroke="#fff"/><polyline points="17,0.5 21,3 17,5.5" fill="none" stroke="#fff"/></svg></a>
    </div>
    <div class="product-shot" role="img" aria-label="Product photo of two infant formula tins"></div>
    <p class="copyright">Tawny Crate.com Copyright All Rights reserved</p>
  </footer>
</body>
</html>
```